Business Card design for Property Developer

We need a business card design for a Melbourne based Property Developer called "Kestrel Grove Pty Ltd".

We subdivide land and onsell to builders etc.

We already have a company logo, which is attached. Also I have attached the layout requirements from the printer. We would like a 2-sided design with one side displaying our logo by itself and the other with the required info, such as name, address, tel no., email, abn etc. The card will need to be used by 4 members of staff so name and contact details should be interchangable.
Updates

If possible, can you please write "name' "job position" "phone" "email" "address" on the card but leave them so I can add the details at a later time. Thank you. Also I plan on printing with UV spot printing as a background on the card. Keep this is mind when designing.

Thanks again.

Hello designers, please do not include pics of houses, house plansĀ or construction machinery etc as we really do not like the way it looks. Thank you.

Target Market(s)

Real Estate Agents, Land Owners, Local Council Departments, Govt Bodies, other Developers etc.

Industry/Entity Type

Business

Requirements
Must have
• 2-sided design with one side displaying our logo by itself and the other with the required info, such as name, address, tel no., email, abn etc.

```html
<!DOCTYPE html>
<html lang="en">
<head>
<meta charset="utf-8">
<title>Kestrel Grove – Business Card</title>
<link rel="stylesheet" href="https://fonts.googleapis.com/css2?family=Archivo:ital,wght@0,400;0,800;1,800&display=swap">
<style>
  :root {
    --page: #ffffff;
    --card: #f7f7f7;
    --card-edge: #d9d9d9;
    --brand-red: #b5121b;
    --brand-blue: #2f6fb8;
    --ink-navy: #1f2a7a;
    --ink-blue: #2c3c95;
    --pattern-light: #ffffff;
    --pattern-mid: #ececec;
  }
  * { margin: 0; padding: 0; box-sizing: border-box; }
  html, body {
    width: 1200px; height: 658px; overflow: hidden;
    background: var(--page);
    font-family: "Archivo", Arial, sans-serif;
  }
  .sheet { position: relative; width: 1200px; height: 658px; }
  .card {
    position: absolute; top: 157px;
    width: 515px; height: 325px;
    background: var(--card);
    border: 1px solid var(--card-edge);
    box-shadow: 0 2px 5px rgba(0,0,0,0.18);
    overflow: hidden;
  }
  .card--front { left: 58px; }
  .card--back { left: 627px; }

  .front-pattern {
    position: absolute; inset: 0;
    background: radial-gradient(ellipse at 50% 45%, var(--pattern-light) 0%, var(--pattern-mid) 100%);
  }
  .front-brand {
    position: absolute; left: 0; right: 0; top: 84px;
    display: flex; flex-direction: column; align-items: center;
  }
  .brand-dot {
    width: 104px; height: 104px; border-radius: 50%;
    background: var(--brand-blue);
  }
  .brand-name {
    margin-top: 22px;
    font-weight: 800; font-size: 38px; letter-spacing: 0.5px;
    color: var(--brand-red); text-transform: uppercase;
  }

  .back-decor {
    position: absolute; right: -40px; top: 0; width: 300px; height: 325px;
    background: radial-gradient(circle at 70% 45%, var(--pattern-mid) 0%, var(--card) 70%);
  }
  .back-brand {
    position: absolute; left: 38px; top: 34px;
    display: flex; flex-direction: column; align-items: flex-start;
  }
  .back-brand .brand-dot { width: 44px; height: 44px; margin-left: 40px; }
  .back-brand .brand-name { margin-top: 6px; font-size: 17px; }

  .holder { position: absolute; left: 45px; top: 130px; }
  .holder-name {
    font-weight: 800; font-size: 18px; color: var(--ink-navy); text-transform: uppercase;
  }
  .holder-title {
    font-weight: 800; font-style: italic; font-size: 13px; color: var(--ink-navy);
    margin-left: 4px; letter-spacing: 0.6px;
  }
  .contact {
    position: absolute; left: 45px; top: 178px;
    display: grid; grid-template-columns: 48px auto;
    row-gap: 2px; font-size: 13.5px; line-height: 16px; color: var(--ink-blue);
  }
</style>
</head>
<body>
<div class="sheet">
  <section class="card card--front">
    <div class="front-pattern" role="img" aria-label="Faint repeating brand-mark pattern for UV spot print"></div>
    <div class="front-brand">
      <div class="brand-dot"></div>
      <div class="brand-name">Kestrel Grove</div>
    </div>
  </section>

  <section class="card card--back">
    <div class="back-decor" role="img" aria-label="Large faint brand-mark decoration"></div>
    <div class="back-brand">
      <div class="brand-dot"></div>
      <div class="brand-name">Kestrel Grove</div>
    </div>
    <div class="holder">
      <div class="holder-name">Firstname Lastname</div>
      <div class="holder-title">Position Title</div>
    </div>
    <div class="contact">
      <span>Tel:</span><span>0400 555 019</span>
      <span>Email:</span><span>Name@KestrelGrove.com</span>
      <span>Mail:</span><span>Street Address Line 1</span>
      <span></span><span>City, Australia, Postal Code</span>
      <span>Web:</span><span>www.KestrelGrove.com</span>
      <span>ABN:</span><span>12 345 678 901</span>
    </div>
  </section>
</div>
</body>
</html>
```